Brochure Design Project

Our company is KMV Sable Ridge. (no LOGO)

We are a restaurant marketing and advertising service. We market restaurants menus by producing a menu guide, distributing flyers and post cards, and also placing the restaurants menu on our website for delivery.

We make restaurants more profitable, by making their food more accessible. Marketing restaurants on search engines, websites, plazanet, wunq, zintro, and a total of 21 different marketing techniques that make restaurants more money.

Key Point: This is all done at NO COST to the restaurant.

We are looking for a design for a brochure that will be mailed as well as handed to restaurateurs.

In my attached file I am including our sales letter. The letter can stay in letter form for the inside of a tri-fold brochure or it can be part of your design.

For more information about our service, please read the attached sales letter.
Updates

Target Market(s)

Restaurant Owners and General managers

Industry/Entity Type

Advertising

Requirements
Must have
• Must look attractive and Eye-catching

```html
<!DOCTYPE html>
<html lang="en">
<head>
<meta charset="utf-8">
<title>KMV Sable Ridge – Tri-fold Brochure</title>
<link href="https://fonts.googleapis.com/css2?family=Play:wght@400;700&family=Open+Sans:wght@400;600;700&family=Arimo:wght@700&display=swap" rel="stylesheet">
<style>
  :root{
    --page:#d9d6d2;
    --paper:#ffffff;
    --panel-grey:#e6e6e8;
    --bar:#3d3e42;
    --ink:#3f4043;
    --ink-soft:#555659;
    --lime:#a8cf3c;
    --bubble:#f3c81c;
    --photo-light:#7fb3dc;
    --photo-dark:#1d4f85;
  }
  *{margin:0;padding:0;box-sizing:border-box}
  html,body{width:1200px;height:892px;overflow:hidden;background:var(--page)}
  .brochure{position:absolute;left:40px;top:52px;width:1112px;height:786px;background:var(--paper);overflow:hidden}
  .bar{position:absolute;left:0;width:100%;height:10px;background:var(--bar)}
  .bar--top{top:10px}
  .bar--bottom{top:766px}
  .panel{position:absolute;top:20px;height:746px}
  .panel--left{left:0;width:370px}
  .panel--middle{left:370px;width:370px}
  .panel--right{left:740px;width:372px}
  .block-grey{position:absolute;left:0;width:100%;background:var(--panel-grey)}
  .photo-band{position:absolute;left:370px;top:0;width:742px;height:786px}

  .tired{position:absolute;left:22px;top:27px;font:400 25px/34px "Play",sans-serif;color:var(--ink);text-transform:uppercase;letter-spacing:.3px}
  .call-now{position:absolute;left:24px;top:172px;font:700 45px/1 "Play",sans-serif;color:var(--ink)}
  .about-title{position:absolute;left:24px;top:292px;font:700 21px/1 "Open Sans",sans-serif;color:var(--ink)}
  .about-text{position:absolute;left:24px;top:324px;width:310px;font:400 13px/20px "Open Sans",sans-serif;color:var(--ink);text-align:justify}
  .about-text strong{font-weight:700}
  .bubble{position:absolute;left:22px;top:444px}
  .reach{position:absolute;left:116px;top:480px;font:700 20px/26px "Open Sans",sans-serif;color:var(--ink)}
  .reach-text{position:absolute;left:24px;top:546px;width:318px;font:400 13.5px/26.3px "Open Sans",sans-serif;color:var(--ink);text-align:justify;letter-spacing:.3px}

  .service{position:absolute;left:31px;top:18px;font:400 24px/32px "Play",sans-serif;color:var(--ink-soft)}
  .consult{position:absolute;left:31px;top:137px;width:310px;font:700 14px/21px "Open Sans",sans-serif;color:var(--ink-soft);letter-spacing:.3px}
  .contact{position:absolute;left:31px;top:596px;font:700 25px/32px "Open Sans",sans-serif;color:var(--ink)}

  .brand{position:absolute;left:0;top:26px;width:100%;text-align:center;font:400 46px/52px "Open Sans",sans-serif;color:var(--ink)}
  .promise{position:absolute;left:0;top:556px;width:100%;text-align:center;font:700 22px/34.5px "Arimo",sans-serif;color:var(--ink);text-transform:uppercase;letter-spacing:.5px}
</style>
</head>
<body>
<main class="brochure">
  <div class="bar bar--top"></div>

  <section class="panel panel--left">
    <div class="block-grey" style="top:275px;height:471px"></div>
    <h2 class="tired">Are you tired of<br>ineffective<br>marketing and<br>advertising?</h2>
    <p class="call-now">Call Us Now</p>
    <h3 class="about-title">About Us</h3>
    <p class="about-text"><strong>KMV Sable Ridge</strong> Is A Restaurant Marketing And Advertising Service That Specializes In Delivery. We Deliver Food From A Variety Of Restaurants To People At Their Homes, Offices Or Hotel Rooms.</p>
    <svg class="bubble" width="94" height="86" viewBox="0 0 94 86" aria-hidden="true">
      <path d="M46 3C22 3 3 17 3 35c0 14 12 26 29 30l-4 18 22-17c22-1 41-15 41-31C91 17 71 3 46 3z" fill="var(--bubble)" stroke="#9a7d12" stroke-width="1.5"/>
    </svg>
    <h3 class="reach">Reach More<br>Potential Customers!</h3>
    <p class="reach-text">Your Customers Are Searching Your Business And Making Their Decisions Online More Than Ever. KMV Sable Ridge Helps You Reach Thousands Of Potential Customers On Search Engines And Social Media Platforms. We Manage Online Advertising So You Don't Miss Out On Any Additional Business.</p>
  </section>

  <section class="panel panel--middle">
    <div class="block-grey" style="top:0;height:300px"></div>
    <h2 class="service">Restaurant Marketing<br>and Advertising<br>specializing in Delivery</h2>
    <p class="consult">To schedule a 15 min consultation that is guaranteed to NOT cost you anthing and only make your restaurant money.</p>
    <p class="contact">Call Rowan Tessle Now<br>555-014-2297<br>or Visit<br>www.kmvsableridge.com</p>
  </section>

  <section class="panel panel--right">
    <div class="block-grey" style="top:470px;height:276px"></div>
    <h1 class="brand">KMV<br>SABLE RIDGE</h1>
    <p class="promise">We make restaurants<br>more profitable,<br>by making their<br>food more<br>accessible!</p>
  </section>

  <svg class="photo-band" viewBox="0 0 742 786" aria-hidden="false">
    <defs>
      <linearGradient id="photoTone" x1="0" y1="0" x2="1" y2="0.3">
        <stop offset="0" stop-color="var(--photo-light)"/>
        <stop offset="0.45" stop-color="var(--photo-dark)"/>
        <stop offset="0.75" stop-color="#2b2d33"/>
        <stop offset="1" stop-color="var(--photo-light)"/>
      </linearGradient>
      <linearGradient id="limeFade" x1="0" y1="0" x2="1" y2="0">
        <stop offset="0" stop-color="var(--lime)"/>
        <stop offset="1" stop-color="var(--lime)" stop-opacity="0"/>
      </linearGradient>
      <linearGradient id="limeFadeIn" x1="0" y1="0" x2="1" y2="0">
        <stop offset="0" stop-color="var(--lime)" stop-opacity="0"/>
        <stop offset="1" stop-color="var(--lime)"/>
      </linearGradient>
    </defs>
    <polygon points="0,292 370,226 742,163 742,460 370,546 0,600" fill="url(#photoTone)" role="img" aria-label="Photo: two business people in suits smiling at a laptop in front of blue glass office towers"/>
    <polygon points="0,292 370,226 370,236 0,304" fill="url(#limeFade)"/>
    <polygon points="370,536 742,452 742,464 370,548" fill="url(#limeFadeIn)"/>
  </svg>

  <div class="bar bar--bottom"></div>
</main>
</body>
</html>
```